Website design for Brelvo Quad

Full Website Content Draft for: 'Brelvo Quad - A Financial Freedom Movement'

Header / Navigation
Logo (top left)
Navigation Links: Home | Our Story | Current State | Future State | How You Can Help | The Movement | Get Involved
CTA Button: Join the Movement
Homepage (Hero Section)

Headline:
Empowering Students. Transforming Futures.
Sub-Headline:
Financial literacy isn’t optional anymore — it’s essential.
Body (short):
Every year, millions of college students step into adulthood without the skills to manage money wisely. It’s time to change that.
Call-to-Action Button:
[Join the Movement]
Visual Suggestion:
Full-width image/video of diverse students on campus — upbeat, collaborative, inspiring.
Our Story

Section Header: Our Story
Body Copy:
For too long, financial literacy has been the missing piece of higher education. While students prepare academically for their futures, many graduate with financial stress, poor money habits, and debt that follows them for decades.
We believe knowledge is power — and financial literacy is freedom. With decades of combined experience in banking, leadership, and higher education, our team has seen the struggles firsthand. That’s why we’re committed to starting a movement that ensures every student leaves college not only with a degree, but with financial confidence.
The Current State

Section Header: The Current State
Infographic Copy / Stats:
70% of college students report finances as their #1 source of stress.*
43% of students don’t know their credit score.**
Student loan debt has surpassed $1.7 trillion.***
Subtext:
This is today’s reality. Students deserve better.
Footnotes (to place at bottom of page):
* Norwell Scholastic Wellness Guild, Kestrin Student Vitality Survey, Spring 2022 Report.
** DALMOR & Pexton Pension Partners, Coins Count at School Review (2019).
*** Quillan Monetary Trust of Harbridge, Consumer Credit Data (2024).
Visual Suggestion:
Infographic row with 3 icons (stress, credit, debt) and corresponding stats.
The Future State (Vision)

Section Header: The Future State (Vision)
Body Copy:
Imagine a campus where students graduate with more than a degree — they graduate with financial confidence.
They know how to budget, save, manage credit, and plan for their futures. They are free from fear, better equipped for life after graduation, and ready to thrive personally and professionally.
This is the future we are building together.
Visual Suggestion:
Smiling students celebrating graduation, overlay text “Confidence. Knowledge. Freedom.”
How You Can Help

Section Header: How You Can Help
Copy with Columns:
Universities
Partner with us to bring scalable, student-centered financial education to your campus.
Banks & Financial Institutions
Join us in shaping the next generation of financially confident customers while strengthening community impact.
Students & Parents
Be part of a movement that makes the college experience stronger, not harder.
Call-to-Action Button:
[Contact Us to Partner]
Visual Suggestion:
Three-column layout with icons (graduation cap for Universities, bank building for Banks, heart/people for Students & Parents).
The Movement

Section Header: The Movement
Body Copy:
This isn’t about one campus — it’s about a shift. A national movement to change the financial future for an entire generation. Together, we can rewrite the story.
We believe when students understand money, they reduce stress, gain freedom, and unlock their potential. That’s why this is more than a program — it’s a movement.
Visual Suggestion:
Map of the U.S. with “movement dots” spreading out, or collage of diverse students with bold words: Financial Literacy. Confidence. Future.
Get Involved (Contact Section)

Section Header: Get Involved
Body Copy:
Are you a university leader, bank executive, student, or parent who wants to be part of this movement? Let’s talk.
Contact Form Fields:
Name
Email
Role (University Faculty/Staff, Bank Partner, Student, Parent, Other)
Message
CTA Button: [Submit Interest]
Footer

Copy:
Join us in building the future of financial literacy.
Links: Privacy | Contact | Social Media (Workloom, Snapvale, etc.)

Target Market(s)

Partners: University Faculty and Bank Executives

Industry/Entity Type

Finance and Education

Coding

Number of Pages Required

4 page

Font styles to use
Sans Serif

Colors

Designer to choose colors to be used in the design.

Requirements
Nice to have
• See description for details - This is a website to create a "movement" to help college and university students increase their financial literacy and reduce financial stress,

```html
<!DOCTYPE html>
<html lang="en">
<head>
<meta charset="utf-8">
<title>Brelvo Quad – A Financial Freedom Movement</title>
<link rel="stylesheet" href="https://fonts.googleapis.com/css2?family=Poppins:wght@400;500;600;700&family=Figtree:wght@500;600;700;800&display=swap">
<style>
:root{
  --blue:#0b4aa8;
  --blue-deep:#08388a;
  --sky:#1e88e5;
  --ink:#111827;
  --muted:#5b6472;
  --panel:#e6eef8;
  --line:#dbe5f1;
  --white:#ffffff;
}
*{box-sizing:border-box;margin:0;padding:0}
html,body{width:1200px;height:4024px;overflow:hidden;background:var(--white)}
body{font-family:'Poppins',sans-serif;color:var(--ink);position:relative}
.abs{position:absolute}
h1,h2,h3,.logo{font-family:'Figtree',sans-serif}
.title{font-size:36px;font-weight:600;color:var(--ink);display:inline-flex;align-items:flex-start;gap:2px;line-height:1}
.title svg{width:16px;height:16px;margin-top:-6px}
.btn{display:inline-flex;align-items:center;justify-content:center;gap:10px;background:var(--blue);color:var(--white);font-family:'Figtree',sans-serif;font-weight:700;font-size:15px;border-radius:30px;text-decoration:none}
.btn-sky{background:#1473d6}
.btn svg{width:12px;height:12px}

/* nav */
.nav{left:0;top:0;width:1200px;height:83px;display:flex;align-items:center;border-bottom:1px solid var(--line)}
.logo{font-weight:800;color:var(--ink);line-height:1;text-align:center}
.nav .logo{position:absolute;left:50px;top:16px;font-size:34px}
.logo small{display:block;font-size:16px;font-weight:800}
.nav ul{position:absolute;left:222px;top:30px;display:flex;gap:19px;list-style:none;font-size:14px;font-weight:500}
.nav li.active{color:var(--sky)}
.nav .btn{position:absolute;left:970px;top:18px;width:180px;height:46px}

/* hero */
.hero{left:0;top:83px;width:1200px;height:561px;background:linear-gradient(100deg,#3d3a36 0%,#6b6359 40%,#9a8f80 70%,#5c6470 100%)}
.hero .shade{position:absolute;inset:0;background:linear-gradient(90deg,rgba(10,20,40,.55),rgba(10,20,40,.15) 60%,rgba(0,0,0,0))}
.hero h1{position:absolute;left:143px;top:110px;font-size:48px;font-weight:700;color:var(--white);line-height:60px}
.hero h1 span{color:#3aa0ff}
.hero .tag{position:absolute;left:143px;top:242px;font-size:17px;font-weight:500;color:var(--white)}
.hero .body{position:absolute;left:143px;top:284px;width:490px;font-size:14px;line-height:24px;color:#eef2f7}
.hero .btn{position:absolute;left:144px;top:365px;width:239px;height:52px;font-size:16px}

/* story */
.photo{border-radius:10px}
.story-photo{left:144px;top:703px;width:456px;height:461px;background:linear-gradient(160deg,#c9d5c0,#8d9a80 45%,#b4a48e 75%,#d8d2c6)}
.story-text{left:652px;top:742px;width:404px}
.story-text p{font-size:13.5px;line-height:23.5px;color:var(--muted);text-align:justify;margin-top:10px}
.story-text .title{margin-bottom:26px}
.story-text .btn{margin-top:34px;width:164px;height:46px}

/* current state */
.cs-title{left:0;top:1236px;width:1200px;text-align:center}
.track{left:144px;top:1327px;width:911px;height:24px;background:linear-gradient(90deg,rgba(220,232,246,0),#dde8f5 15%,#dde8f5 85%,rgba(220,232,246,0))}
.bubble{width:72px;height:72px;border-radius:50%;background:#c7d9ef;display:flex;align-items:center;justify-content:center}
.bubble svg{width:40px;height:40px}
.bubble.on{background:var(--blue)}
.card{background:var(--white);border-radius:6px;box-shadow:0 2px 12px rgba(20,40,80,.08);text-align:center;padding-top:32px}
.card h3{font-family:'Poppins',sans-serif;font-size:17px;font-weight:500}
.card p{font-size:13.5px;line-height:23px;color:var(--muted);margin:14px auto 0;width:240px}
.card.on{background:var(--blue);color:var(--white)}
.card.on p{color:var(--white)}
.cs-sub{left:0;top:1568px;width:1200px;text-align:center;font-size:17px;font-weight:500}

/* future */
.future{left:142px;top:1732px;width:404px}
.future .lead{font-size:16.5px;line-height:27px;color:var(--blue);margin-top:24px}
.future p{font-size:13.5px;line-height:23.5px;color:var(--muted);text-align:justify;margin-top:10px}
.future em{display:block;font-size:14px;color:var(--ink);margin-top:10px}
.future-photo{left:600px;top:1667px;width:600px;height:399px;border-radius:14px 0 0 14px;background:linear-gradient(170deg,#5e8fd0,#a9c6ea 45%,#6a6258 78%,#2e2a2a)}
.future-photo .over{position:absolute;left:31px;top:28px;font-family:'Figtree',sans-serif;font-weight:800;font-size:37px;line-height:48px;color:var(--white)}

/* help */
.help-title{left:142px;top:2160px}
.help-btn{left:820px;top:2159px;width:235px;height:46px;font-size:15px}
.help-card{background:var(--panel);border-radius:4px;text-align:center;padding-top:27px}
.help-card .ic{width:84px;height:84px;border-radius:50%;background:var(--blue);margin:0 auto;display:flex;align-items:center;justify-content:center}
.help-card .ic svg{width:48px;height:48px}
.help-card h3{font-family:'Poppins',sans-serif;font-weight:500;font-size:17px;margin-top:20px}
.help-card p{font-size:13.5px;line-height:23.5px;color:var(--muted);width:262px;margin:10px auto 0}

/* movement */
.movement{left:0;top:2570px;width:1200px;text-align:center;font-family:'Figtree',sans-serif;font-weight:800;font-size:42px;color:var(--ink)}
.movement span{color:#1268d0}
.movement-photo{left:0;top:2640px;width:1200px;height:566px;background:linear-gradient(90deg,#6a5244 0%,#b8c3bf 22%,#b7a08a 42%,#e5e2dc 55%,#8697ab 72%,#ddd6c8 100%)}
.movement-photo::after{content:"";position:absolute;inset:0;background:linear-gradient(180deg,#fff 0%,rgba(255,255,255,0) 18%)}

/* involved */
.gi-title{left:0;top:3280px;width:1200px;text-align:center}
.gi-sub{left:0;top:3338px;width:1200px;text-align:center;font-size:14px}
.field{background:var(--panel);border-radius:6px;font-size:11px;color:var(--muted);padding:0 18px;display:flex;align-items:center;gap:6px}
.field svg{width:10px;height:10px}
.field.msg{align-items:flex-start;padding-top:17px}
.field .chev{margin-left:auto}
.gi-btn{left:502px;top:3598px;width:195px;height:47px}

/* footer */
.footer{left:0;top:3723px;width:1200px;height:301px;background:var(--blue);color:var(--white)}
.footer .logo{position:absolute;left:0;width:1200px;top:58px;color:var(--white);font-size:38px}
.footer .logo small{font-size:17px}
.rule{position:absolute;left:144px;width:911px;height:1px;background:rgba(255,255,255,.3)}
.note{position:absolute;top:144px;font-size:13.5px;line-height:23px;display:flex;gap:7px}
.note svg{flex:none;width:13px;height:13px;margin-top:5px}
.foot-links{position:absolute;left:144px;top:266px;font-size:13.5px}
.social{position:absolute;left:574px;top:265px;display:flex;gap:8px;font-size:11px;align-items:center}
.social i{width:20px;height:20px;border-radius:50%;background:rgba(255,255,255,.2);display:inline-block}
.copy{position:absolute;right:145px;top:266px;font-size:13.5px}
</style>
</head>
<body>

<header class="abs nav">
  <div class="logo">Brelvo<small>Quad</small></div>
  <ul>
    <li class="active">Home</li><li>Our Story</li><li>Current State</li><li>Future State</li><li>How You Can Help</li><li>The Movement</li><li>Get Involved</li>
  </ul>
  <a class="btn" href="#">Join The Movement</a>
</header>

<section class="abs hero" role="img" aria-label="Students walking together across a sunny campus">
  <div class="shade"></div>
  <h1><span>| Empowering</span> Students.<br>Transforming Futures.</h1>
  <p class="tag">Financial Literacy Isn’t Optional Anymore It’s Essential.</p>
  <p class="body">Every year, millions of college students step into adulthood without the skills to manage money wisely. It’s time to change that.</p>
  <a class="btn btn-sky" href="#">Join The Movement <svg viewBox="0 0 12 12"><path d="M2 10L10 2M4 2h6v6" stroke="#fff" stroke-width="1.6" fill="none"/></svg></a>
</section>

<div class="abs photo story-photo" role="img" aria-label="Group of smiling students walking in front of a university building"></div>
<section class="abs story-text">
  <h2 class="title">Our Story<svg viewBox="0 0 16 16"><path d="M0 2L16 0 12 16 11 5z" fill="#1e88e5"/></svg></h2>
  <p>For too long, financial literacy has been the missing piece of higher education. While students prepare academically for their futures, many graduate with financial stress, poor money habits, and debt that follows them for decades.</p>
  <p>We believe knowledge is power — and financial literacy is freedom. With decades of combined experience in banking, leadership, and higher education, our team has seen the struggles firsthand. That’s why we’re committed to starting a movement that ensures every student leaves college not only with a degree, but with financial confidence.</p>
  <a class="btn" href="#">Learn More <svg viewBox="0 0 12 12"><path d="M2 10L10 2M4 2h6v6" stroke="#fff" stroke-width="1.6" fill="none"/></svg></a>
</section>

<div class="abs cs-title"><h2 class="title">The Current State<svg viewBox="0 0 16 16"><path d="M0 2L16 0 12 16 11 5z" fill="#1e88e5"/></svg></h2></div>
<div class="abs track"></div>
<div class="abs bubble" style="left:253px;top:1303px"><svg viewBox="0 0 40 40" fill="none" stroke="#0b4aa8" stroke-width="1.8"><path d="M14 34v-6c-4-2-6-6-6-10a12 12 0 0124 0l3 6h-3v5h-5v5"/><circle cx="20" cy="17" r="4"/></svg></div>
<div class="abs bubble on" style="left:564px;top:1303px"><svg viewBox="0 0 40 40" fill="none" stroke="#fff" stroke-width="1.8"><rect x="6" y="10" width="26" height="18" rx="2"/><path d="M6 16h26"/><circle cx="29" cy="27" r="6" fill="#0b4aa8"/><path d="M26 27l2 2 4-4"/></svg></div>
<svg class="abs" style="left:590px;top:1372px" width="20" height="12" viewBox="0 0 20 12"><path d="M0 0h20L10 12z" fill="#0b4aa8"/></svg>
<div class="abs bubble" style="left:875px;top:1303px"><svg viewBox="0 0 40 40" fill="none" stroke="#0b4aa8" stroke-width="1.8"><circle cx="14" cy="16" r="7"/><path d="M11 19l6-6M11 13h1M16 19h1"/><circle cx="26" cy="22" r="6"/><path d="M26 19v6M24 21h3"/><path d="M6 32l8-4h12l6-3"/></svg></div>

<div class="abs card" style="left:144px;top:1403px;width:289px;height:136px"><h3>STRESS</h3><p>70% of college students report finances as their #1 source of stress.</p></div>
<div class="abs card on" style="left:455px;top:1403px;width:289px;height:136px"><h3>CREDIT</h3><p>43% of students don’t know their credit score.</p></div>
<div class="abs card" style="left:767px;top:1403px;width:288px;height:136px"><h3>DEBT</h3><p>Student loan debt has surpassed $1.7 trillion.</p></div>
<p class="abs cs-sub">This Is Today’s Reality. Students Deserve Better.</p>

<section class="abs future">
  <h2 class="title">The Future State<svg viewBox="0 0 16 16"><path d="M0 2L16 0 12 16 11 5z" fill="#1e88e5"/></svg></h2>
  <p class="lead">Imagine a campus where students graduate with more than a degree  they graduate with financial confidence.</p>
  <p>They know how to budget, save, manage credit, and plan for their futures. They are free from fear, better equipped for life after graduation, and ready to thrive personally and professionally.</p>
  <em>This is The Future We Are Building Together.</em>
</section>
<div class="abs future-photo" role="img" aria-label="Graduates in gowns tossing caps into a blue sky in front of a campus building">
  <div class="over">Confidence.<br>Knowledge.<br>Freedom.</div>
</div>

<div class="abs help-title"><h2 class="title">How You Can Help<svg viewBox="0 0 16 16"><path d="M0 2L16 0 12 16 11 5z" fill="#1e88e5"/></svg></h2></div>
<a class="abs btn help-btn" href="#">Contact Us to Partner <svg viewBox="0 0 12 12"><path d="M2 10L10 2M4 2h6v6" stroke="#fff" stroke-width="1.6" fill="none"/></svg></a>

<div class="abs help-card" style="left:145px;top:2234px;width:287px;height:274px">
  <div class="ic"><svg viewBox="0 0 48 48" fill="none" stroke="#fff" stroke-width="1.8"><path d="M8 20h32L24 10z"/><path d="M10 20v18h28V20M6 38h36"/><rect x="19" y="25" width="10" height="9"/><path d="M30 9l8-3 8 3-8 3z"/></svg></div>
  <h3>Universities</h3>
  <p>Partner with us to bring scalable, student-centered financial education to your campus.</p>
</div>
<div class="abs help-card" style="left:456px;top:2234px;width:287px;height:274px">
  <div class="ic"><svg viewBox="0 0 48 48" fill="none" stroke="#fff" stroke-width="1.8"><path d="M6 18h36L24 8z"/><path d="M10 18v18M38 18v18M6 40h36M8 36h32"/><circle cx="24" cy="27" r="6"/><path d="M24 23v8"/></svg></div>
  <h3>Banks &amp; Financial Institutions</h3>
  <p>Join us in shaping the next generation of financially confident customers while strengthening community impact.</p>
</div>
<div class="abs help-card" style="left:767px;top:2234px;width:288px;height:274px">
  <div class="ic"><svg viewBox="0 0 48 48" fill="none" stroke="#fff" stroke-width="1.8"><path d="M24 40L9 25a8 8 0 0115-9 8 8 0 0115 9z"/><circle cx="18" cy="22" r="3"/><circle cx="30" cy="22" r="3"/><path d="M13 32c1-3 3-5 5-5s4 2 6 5c2-3 4-5 6-5s4 2 5 5"/></svg></div>
  <h3>Students and Parents</h3>
  <p>Be part of a movement that makes the college experience stronger, not harder.</p>
</div>

<h2 class="abs movement">FINANCIAL <span>LITERACY</span>. CONFIDENCE. <span>FUTURE</span>.</h2>
<div class="abs movement-photo" role="img" aria-label="Five diverse smiling students holding notebooks and coffee"></div>

<div class="abs gi-title"><h2 class="title">Get Involved<svg viewBox="0 0 16 16"><path d="M0 2L16 0 12 16 11 5z" fill="#1e88e5"/></svg></h2></div>
<p class="abs gi-sub">Are You A University Leader, Bank Executive, Student, or Parent Who Wants To Be Part of This Movement? Let’s Talk.</p>
<div class="abs field" style="left:180px;top:3386px;width:410px;height:47px"><svg viewBox="0 0 10 10"><circle cx="5" cy="3" r="2.5" fill="#5b6472"/><path d="M0 10a5 5 0 0110 0z" fill="#5b6472"/></svg>Full Name*</div>
<div class="abs field" style="left:180px;top:3450px;width:410px;height:47px"><svg viewBox="0 0 10 10"><rect y="2" width="10" height="7" fill="#5b6472"/></svg>Email*</div>
<div class="abs field" style="left:180px;top:3514px;width:410px;height:47px"><svg viewBox="0 0 10 10"><path d="M5 0l1.5 3.5L10 4 7.3 6.3 8 10 5 8 2 10l.7-3.7L0 4l3.5-.5z" fill="#5b6472"/></svg>Role*<svg class="chev" viewBox="0 0 10 10"><path d="M2 3l3 3 3-3" stroke="#5b6472" fill="none"/></svg></div>
<div class="abs field msg" style="left:610px;top:3386px;width:412px;height:176px"><svg viewBox="0 0 10 10"><ellipse cx="5" cy="4.5" rx="5" ry="3.8" fill="#5b6472"/></svg>Message*</div>
<a class="abs btn gi-btn" href="#">Submit Interest <svg viewBox="0 0 12 12"><path d="M2 10L10 2M4 2h6v6" stroke="#fff" stroke-width="1.6" fill="none"/></svg></a>

<footer class="abs footer">
  <div class="logo">Brelvo<small>Quad</small></div>
  <div class="rule" style="top:125px"></div>
  <div class="note" style="left:144px;width:290px"><svg viewBox="0 0 14 14"><circle cx="7" cy="7" r="7" fill="#fff"/><path d="M4 7l2 2 4-4" stroke="#0b4aa8" stroke-width="1.6" fill="none"/></svg><span>Norwell Scholastic Wellness Guild, Kestrin Student Vitality Survey, Spring 2022 Report.</span></div>
  <div class="note" style="left:496px;width:260px"><svg viewBox="0 0 14 14"><circle cx="7" cy="7" r="7" fill="#fff"/><path d="M4 7l2 2 4-4" stroke="#0b4aa8" stroke-width="1.6" fill="none"/></svg><span>DALMOR &amp; Pexton Pension Partners, Coins Count at School Review (2019).</span></div>
  <div class="note" style="left:816px;width:240px"><svg viewBox="0 0 14 14"><circle cx="7" cy="7" r="7" fill="#fff"/><path d="M4 7l2 2 4-4" stroke="#0b4aa8" stroke-width="1.6" fill="none"/></svg><span>Quillan Monetary Trust of Harbridge, Consumer Credit Data (2024).</span></div>
  <div class="rule" style="top:238px"></div>
  <div class="foot-links">PRIVACY &nbsp;|&nbsp; CONTACT</div>
  <div class="social"><i></i>Workloom <i></i>Snapvale</div>
  <div class="copy">© 2025 Brelvo Quad</div>
</footer>

</body>
</html>
```